Lantern Airfields Homepage Design Update

here's the current site - http://lanternairfields.example/

client is not happy with overall look.

keeping the same info - intro text, headlines, featured media excepts and general navigation options - can you come up with a nicer, slicker look for this homepage?

UPDATE: since it was asked by designer.. the general layout doesnt have to be the same. its not required to have a big image, with text below that and then smaller images/text below that. as long as we have the same content on the page, it can organized and designed in any way,

client like big images, so one way or the other, keep that... but feel free to reorganize content, explore different ways of framing it, and/or anything else. make this homepage pop!

for the designer that wins this, we'll start an additional project to update the interior.

let me know if any questions..

thanks!

marcus

Target Market(s)

aviation industry professionals, local governments, general public

Number of Pages Required

1 page

Font styles to use
Sans Serif

Requirements
Must have
• big image somewhere. same content as on current site, just designed differently.

```html
<!DOCTYPE html>
<html lang="en">
<head>
<meta charset="utf-8">
<title>Lantern Airfields</title>
<link href="https://fonts.googleapis.com/css2?family=Roboto:wght@300;400;500;700;900&display=swap" rel="stylesheet">
<style>
:root{
  --ink:#2a2a2a;
  --nav:#4a4a4a;
  --green:#95c90f;
  --green-deep:#4e8a12;
  --green-text:#6bb52a;
  --panel:#e9e9e9;
  --footer:#484c5b;
  --white:#ffffff;
}
*{margin:0;padding:0;box-sizing:border-box}
html,body{width:1199px;height:1200px;overflow:hidden;background:var(--white);font-family:'Roboto',sans-serif}
.page{position:relative;width:1199px;height:1200px}

.site-header{position:absolute;left:0;top:0;width:1199px;height:66px;background:var(--white)}
.brand{position:absolute;left:127px;top:26px;display:flex;align-items:center;gap:7px;font-size:15px;font-weight:400;color:#3a3f5c;letter-spacing:1px}
.brand-dot{width:10px;height:10px;border-radius:50%;background:#3a3f5c}
.main-nav{position:absolute;right:136px;top:32px;display:flex;gap:15px;font-size:10.5px;letter-spacing:1.2px;color:var(--nav);font-weight:400}

.hero{position:absolute;left:0;top:66px;width:1199px;height:525px;overflow:hidden}
.hero-photo{position:absolute;inset:0;background:
  radial-gradient(ellipse 60% 40% at 50% 52%,#9c8068 0%,rgba(156,128,104,0) 70%),
  linear-gradient(180deg,#57525d 0%,#6e6366 35%,#8c7868 62%,#7a7462 82%,#5e6448 100%)}
.hero-photo::after{content:"";position:absolute;left:50%;top:160px;width:780px;height:230px;transform:translateX(-50%);
  background:radial-gradient(ellipse 50% 45% at 50% 50%,rgba(40,34,38,.55) 0%,rgba(40,34,38,0) 100%)}
.hero-title{position:absolute;left:0;right:0;top:53px;text-align:center;color:var(--white);font-weight:700;font-size:31px;line-height:37px;letter-spacing:2.6px}
.hero-arrow{position:absolute;left:599px;top:545px}

.intro{position:absolute;left:0;top:591px;width:1199px;height:513px;background:var(--panel)}
.intro-shape{position:absolute;left:0;top:0}
.intro-copy{position:absolute;left:123px;top:76px;width:460px}
.eyebrow{font-size:15.5px;font-weight:700;color:var(--green-text);letter-spacing:1.6px}
.headline{margin-top:5px;font-size:29px;font-weight:300;color:var(--ink);letter-spacing:2.8px}
.lede{margin-top:22px;font-size:20.5px;font-weight:300;line-height:25.7px;color:var(--ink);letter-spacing:1.6px}
.lede strong{font-weight:700}
.btn{position:absolute;display:flex;align-items:center;justify-content:center;font-size:20px;font-weight:500;letter-spacing:2px}
.btn-dark{left:230px;top:311px;width:170px;height:51px;border:1px solid var(--ink);color:var(--ink)}

.media{position:absolute;left:681px;top:0;width:420px;height:513px;color:var(--white)}
.media-label{position:absolute;left:0;width:420px;top:70px;text-align:center;font-size:29px;font-weight:300;letter-spacing:2.5px}
.media-thumb{position:absolute;left:133px;top:124px;width:154px;height:160px;background:var(--green-deep);padding:4px 4px 10px}
.media-thumb-photo{width:100%;height:100%;background:linear-gradient(180deg,#cfd4d8 0%,#bfc2c4 55%,#9a9c9a 100%)}
.next-story{position:absolute;left:309px;top:271px;font-size:8px;font-weight:700;letter-spacing:1px;color:#24340a}
.media-title{position:absolute;left:0;width:420px;top:318px;text-align:center;font-size:20.5px;font-weight:700;line-height:26px;letter-spacing:2px}
.btn-light{left:133px;top:407px;width:170px;height:51px;border:1px solid var(--white);color:var(--white);font-weight:700}

.site-footer{position:absolute;left:0;top:1104px;width:1199px;height:96px;background:var(--footer);color:var(--white)}
.footer-nav{position:absolute;left:104px;top:29px;display:flex;gap:13px;font-size:9.5px;font-weight:500;letter-spacing:1.1px}
.copyright{position:absolute;left:104px;top:67px;font-size:9.5px;font-weight:500;letter-spacing:1.1px}
.social{position:absolute;left:947px;top:39px;display:flex;gap:4px}
.social span{width:35px;height:35px;border-radius:50%;background:var(--green)}
</style>
</head>
<body>
<div class="page">
  <header class="site-header">
    <div class="brand"><span class="brand-dot"></span>Lantern Airfields</div>
    <nav class="main-nav"><span>ABOUT</span><span>SERVICES</span><span>AIRPORTS</span><span>NEWS &amp; MEDIA</span><span>CONTACT</span><span>EMPLOYEES</span></nav>
  </header>

  <section class="hero">
    <div class="hero-photo" role="img" aria-label="Passenger jet taking off from a runway at dusk"></div>
    <h1 class="hero-title">Bringing private, free enterprise business practices<br>To airports throughout the U.S.</h1>
    <svg class="hero-arrow" width="18" height="10" viewBox="0 0 18 10"><path d="M0 0H18L9 10Z" fill="#fff"/></svg>
  </section>

  <section class="intro">
    <svg class="intro-shape" width="1199" height="513" viewBox="0 0 1199 513"><path d="M574 0H1199V513H568L681 161Z" fill="var(--green)"/></svg>
    <div class="intro-copy">
      <p class="eyebrow">WE DEVELOP P3 AIRPORT OPPORTUNITIES</p>
      <h2 class="headline">WITHIN THE U.S. MARKET</h2>
      <p class="lede">Lantern Airfields is focused on opportunities to <strong>invest</strong>, <strong>develop</strong> and <strong>manage</strong> both general aviation and commercial service airports in key U.S. markets</p>
    </div>
    <a class="btn btn-dark">READ MORE</a>

    <div class="media">
      <h2 class="media-label">Latest Media</h2>
      <div class="media-thumb"><div class="media-thumb-photo" role="img" aria-label="Ground marshal in a safety vest guiding a jet on the apron"></div></div>
      <span class="next-story">NEXT STORY &gt;</span>
      <h3 class="media-title">Plans For Second Airport In<br>Atlanta</h3>
      <a class="btn btn-light">VIEW STORY</a>
    </div>
  </section>

  <footer class="site-footer">
    <nav class="footer-nav"><span>HOME</span><span>ABOUT</span><span>SERVICES</span><span>AIRPORTS</span><span>NEWS &amp; MEDIA</span><span>CONTACT</span><span>EMPLOYEES</span></nav>
    <p class="copyright">© 2015 LANTERN AIRFIELDS. ALL RIGHTS RESERVED</p>
    <div class="social"><span></span><span></span></div>
  </footer>
</div>
</body>
</html>
```